professional looking data specialist website

I've recently had a new logo designed and I'm now looking to get a professional looking website built. This is for a new company that specialises in data. We look to support companies with business intelligence, report modelling, data governance to new european legislation (GDPR). We are offer consultancy or we can attend site and complete work when required. Our target arket is united kingdom wide and we are specifically aiming at small to medium sized companies.

Target Market(s)

small to medium enterprise companies from all industries

Industry/Entity Type

Professional Service

Coding

Coded - Design and coding required

Number of Pages Required

4 page

Font styles to use
Sans Serif

Colors

Designer to choose colors to be used in the design.

Requirements
Must have
• Professional look including the company logo, need to have ability to request more information from us so needs a inquiries page, seperate pages for the different offerings, data governance, report modelling, business intelligence implementation, data protection
Nice to have
• any website interaction, animation, etc
Should not have
• too many colours, too busy pages, must look professional

```html
<!DOCTYPE html>
<html lang="en">
<head>
<meta charset="utf-8">
<title>Northvale Ltd – Data Specialists</title>
<link rel="stylesheet" href="https://fonts.googleapis.com/css2?family=Jost:wght@400;500&family=Open+Sans:ital,wght@0,400;0,600;1,600;1,700&display=swap">
<style>
:root{
  --blue:#0f6db8;
  --blue-dark:#0b5a9a;
  --ink:#222;
  --text:#666;
  --muted:#888;
  --nav:#8c8c8c;
  --line:#e2e2e2;
  --soft:#f7f7f7;
  --white:#fff;
}
*{margin:0;padding:0;box-sizing:border-box}
html,body{width:1200px;height:2663px;overflow:hidden;background:var(--white)}
body{position:relative;font-family:"Open Sans",Arial,sans-serif;color:var(--text)}
.abs{position:absolute}
.heading{font-family:"Jost",Arial,sans-serif;color:var(--ink);font-weight:400}
a{color:inherit;text-decoration:none}

/* header */
.brand{display:flex;align-items:center;gap:10px;font-family:"Jost",Arial,sans-serif;font-weight:500;color:var(--blue)}
.brand-mark{background:var(--blue);display:block}
.site-brand{left:133px;top:40px;font-size:30px}
.site-brand .brand-mark{width:22px;height:22px}
.phone{left:698px;top:38px;display:flex;align-items:center;gap:12px}
.phone-icon{width:40px;height:40px;border:2px solid var(--blue);border-radius:50%;display:flex;align-items:center;justify-content:center}
.phone-label{font-size:11px;color:var(--muted);letter-spacing:.5px}
.phone-number{font-size:18px;color:var(--ink)}
.btn{display:flex;align-items:center;justify-content:center;font-family:"Jost",Arial,sans-serif;font-weight:500;letter-spacing:.5px;font-size:13px;text-transform:uppercase;border:1.5px solid var(--blue);color:var(--blue);background:var(--white)}
.btn::after{content:"";position:absolute;right:-8px;top:-8px;width:10px;height:10px;background:var(--blue);box-shadow:-5px 5px 0 -2px var(--blue)}
.btn-consult{left:911px;top:39px;width:147px;height:41px}

/* nav */
.main-nav{left:0;top:119px;width:1200px;height:51px;background:var(--nav)}
.main-nav ul{list-style:none;display:flex;position:absolute;left:133px;top:0;height:51px}
.main-nav li{height:51px;display:flex;align-items:center;padding:0 14px;color:var(--white);font-family:"Jost",Arial,sans-serif;font-size:13.5px;text-transform:uppercase;border-right:1px solid rgba(255,255,255,.25)}
.main-nav li.active{background:var(--blue);padding:0 24px}

/* hero */
.hero{left:0;top:170px;width:1200px;height:517px;background:linear-gradient(90deg,#eef1f4 0%,#dfe4ea 35%,#c7ced7 60%,#8e969f 85%,#4e5661 100%)}
.hero-kicker{left:133px;top:308px;font-size:32px;line-height:1}
.hero-title{left:131px;top:348px;font-size:50px;line-height:1}
.hero-text{left:133px;top:418px;font-size:16px;line-height:26px;color:#444;width:340px}
.btn-hero{left:133px;top:499px;width:146px;height:39px;background:transparent}
.slider-dots{left:570px;top:662px;display:flex;gap:10px}
.slider-dots span{width:14px;height:4px;background:#556;opacity:.7}
.slider-dots span:first-child{background:var(--blue);opacity:1}

/* what we do */
.section-title{width:1200px;left:0;text-align:center;font-size:30px;text-transform:uppercase}
.wwd-title{top:740px}
.section-sub{left:360px;width:480px;text-align:center;font-size:12.5px;line-height:21px;color:var(--text)}
.wwd-sub{top:778px}
.service{width:260px;font-size:11.5px;line-height:23px;color:var(--muted)}
.service h3{font-family:"Jost",Arial,sans-serif;font-weight:500;font-size:13.5px;color:var(--ink);text-transform:uppercase;margin-bottom:2px}
.service .more{color:var(--blue);font-size:11.5px;display:block;margin-top:2px}
.service.left{text-align:right}
.svc-bi{left:130px;top:866px}
.svc-rm{left:799px;top:866px}
.svc-dg{left:130px;top:1050px}
.svc-cs{left:799px;top:1050px}
.hub{left:420px;top:832px}

/* about band */
.about{left:0;top:1228px;width:1200px;height:472px;background:linear-gradient(160deg,#3b3b3b 0%,#262626 45%,#3f3a33 75%,#1f1f1f 100%)}
.about-title{top:1316px;color:var(--white)}
.play{left:550px;top:1374px}
.about-text{left:230px;top:1496px;width:740px;text-align:center;color:var(--white);font-size:12px;line-height:21px}
.btn-about{left:522px;top:1566px;width:147px;height:37px;background:transparent;color:var(--white);border-color:rgba(255,255,255,.8)}

/* news */
.news{left:0;top:1700px;width:1200px;height:466px;background:var(--soft)}
.news-title{top:1748px}
.card{width:288px;top:1805px}
.card-img{height:187px;border:7px solid var(--white);box-shadow:0 0 0 1px var(--line)}
.card h4{font-family:"Jost",Arial,sans-serif;font-weight:500;font-size:15.5px;color:var(--ink);margin-top:22px}
.card p{font-size:11.5px;line-height:21px;color:var(--muted);margin-top:6px}
.card .meta{display:flex;align-items:center;gap:12px;font-size:11.5px;color:var(--blue);margin-top:9px}
.card .meta i{color:#bbb;font-style:normal}
.card-1{left:133px}.card-2{left:456px}.card-3{left:779px}

/* testimonial */
.quote{left:0;top:2166px;width:1200px;height:163px;background:var(--blue)}
.quote-mark{left:198px;top:2180px;color:var(--white);font-family:"Open Sans",Arial,sans-serif;font-style:italic;font-weight:700;font-size:36px}
.quote-text{left:186px;top:2213px;width:868px;color:var(--white);font-style:italic;font-weight:600;font-size:12.5px;line-height:24.5px}
.arrow{top:2228px}

/* footer */
.footer-brand{left:133px;top:2420px;font-size:36px}
.footer-brand .brand-mark{width:28px;height:28px}
.foot-col h5{font-family:"Jost",Arial,sans-serif;font-weight:500;font-size:16px;color:var(--ink);margin-bottom:14px}
.links{left:414px;top:2365px}
.links ul{list-style:none;font-size:11.5px;line-height:23px;color:#555}
.newsletter{left:605px;top:2365px;width:240px;font-size:11.5px;line-height:20px;color:#555}
.email-field{margin-top:16px;width:229px;height:33px;border:1px solid #d5d5d5;font-size:11px;color:#aaa;padding:0 12px;display:flex;align-items:center;background:var(--white)}
.btn-sub{position:relative;margin-top:27px;width:105px;height:38px;font-size:12px}
.contact{left:919px;top:2365px;font-size:11.5px;line-height:20px;color:#555}
.contact .row{display:flex;gap:16px;align-items:flex-start}
.divider{left:133px;top:2602px;width:934px;height:1px;background:var(--line)}
.copyright{left:128px;top:2620px;font-size:11px;color:#555}
.social{left:940px;top:2614px;display:flex;gap:8px}
.social span{width:27px;height:27px;border:1px solid #aaa;border-radius:50%}
</style>
</head>
<body>

<header>
  <div class="abs brand site-brand"><span class="brand-mark"></span>Northvale Ltd</div>
  <div class="abs phone">
    <span class="phone-icon">
      <svg width="20" height="20" viewBox="0 0 24 24" fill="none" stroke="#0f6db8" stroke-width="2" stroke-linecap="round" stroke-linejoin="round"><path d="M22 16.9v3a2 2 0 0 1-2.2 2 19.8 19.8 0 0 1-8.6-3.1 19.5 19.5 0 0 1-6-6A19.8 19.8 0 0 1 2.1 4.2 2 2 0 0 1 4.1 2h3a2 2 0 0 1 2 1.7c.1.9.4 1.8.7 2.7a2 2 0 0 1-.5 2.1L8 9.8a16 16 0 0 0 6 6l1.3-1.3a2 2 0 0 1 2.1-.4c.9.3 1.8.6 2.7.7a2 2 0 0 1 1.7 2z"/></svg>
    </span>
    <div><div class="phone-label">PHONE :</div><div class="phone-number">(+345) 555-0142</div></div>
  </div>
  <a class="abs btn btn-consult">Free Consulting</a>
</header>

<nav class="abs main-nav">
  <ul>
    <li class="active">Home</li><li>About Us</li><li>Data Governance</li><li>Report Modelling</li><li>Business Intelligence</li><li>Data Protection</li><li>Inquiries</li><li>Contact Us</li>
  </ul>
</nav>

<section>
  <div class="abs hero" role="img" aria-label="Photo of three smiling colleagues working together at a laptop in a bright office"></div>
  <div class="abs heading hero-kicker">BUSINESS</div>
  <h1 class="abs heading hero-title">INTELLIGENCE</h1>
  <p class="abs hero-text">Aliquip ex ea commodo consequat irure dolor in reprehenderit in voluptate velit...</p>
  <a class="abs btn btn-hero">Learn More Info</a>
  <div class="abs slider-dots"><span></span><span></span><span></span></div>
</section>

<section>
  <h2 class="abs heading section-title wwd-title">What We Do</h2>
  <p class="abs section-sub wwd-sub">Lorem ipsum dolor sit amet, consectetur adipiscing elit, sed do eiusmod tempor incididunt labore et dolore magna aliqua</p>

  <svg class="abs hub" width="360" height="360" viewBox="0 0 360 360">
    <circle cx="180" cy="180" r="150" fill="none" stroke="#9a9a9a" stroke-width="5"/>
    <rect x="95" y="112" width="170" height="108" rx="6" fill="#1b1b1b"/>
    <rect x="103" y="120" width="154" height="92" fill="#fff"/>
    <path d="M78 220h204l-10 10H88z" fill="#bdbdbd"/>
    <rect x="166" y="140" width="14" height="14" fill="#0f6db8"/>
    <text x="180" y="185" text-anchor="middle" font-family="Jost, Arial, sans-serif" font-weight="500" font-size="20" fill="#0f6db8">Northvale Ltd</text>
    <g fill="#0f6db8" stroke="#fff" stroke-width="4">
      <circle cx="34" cy="70" r="39"/><circle cx="315" cy="70" r="39"/>
      <circle cx="34" cy="290" r="39"/><circle cx="315" cy="290" r="39"/>
    </g>
    <g fill="none" stroke="#fff" stroke-width="2" stroke-linecap="round" stroke-linejoin="round">
      <path d="M26 80c0-6-8-9-8-18a16 16 0 0 1 32 0c0 9-8 12-8 18z"/><path d="M27 85h14M29 90h10"/>
      <path d="M34 42v-5M14 50l-4-3M54 50l4-3"/>
      <rect x="301" y="52" width="28" height="36" rx="2"/><path d="M309 52v-4h12v4M307 62h3M313 62h12M307 70h3M313 70h12M307 78h3M313 78h12"/>
      <path d="M18 278h12l4 5h18v22H18z"/><rect x="30" y="290" width="10" height="9"/><path d="M32 290v-3a3 3 0 0 1 6 0v3"/>
      <path d="M297 290l10-10 8 4 8-4 10 10-14 13-4-3-4 3z"/><path d="M307 293l6 5M312 289l6 5"/>
    </g>
  </svg>

  <div class="abs service left svc-bi"><h3>Business Intelligence</h3>Aliquip ex ea commodo consequat. Duis aute irure<br>dolor in reprehenderit in voluptate velit esse cillum<br>dolore eu fugiat nulla pariatur...<span class="more">Learn More Info +</span></div>
  <div class="abs service svc-rm"><h3>Report Modelling</h3>Aliquip ex ea commodo consequat. Duis aute irure<br>dolor in reprehenderit in voluptate velit esse cillum<br>dolore eu fugiat nulla pariatur...<span class="more">Learn More Info +</span></div>
  <div class="abs service left svc-dg"><h3>Data Governance</h3>Aliquip ex ea commodo consequat. Duis aute irure<br>dolor in reprehenderit in voluptate velit esse cillum<br>dolore eu fugiat nulla pariatur...<span class="more">Learn More Info +</span></div>
  <div class="abs service svc-cs"><h3>Consultancy</h3>Aliquip ex ea commodo consequat. Duis aute irure<br>dolor in reprehenderit in voluptate velit esse cillum<br>dolore eu fugiat nulla pariatur...<span class="more">Learn More Info +</span></div>
</section>

<section>
  <div class="abs about" role="img" aria-label="Dark photo of hands typing on a keyboard at a desk with a monitor and notes"></div>
  <h2 class="abs heading section-title about-title">About Northvale Ltd</h2>
  <svg class="abs play" width="100" height="100" viewBox="0 0 100 100"><circle cx="50" cy="50" r="46" fill="rgba(0,0,0,.35)" stroke="#fff" stroke-width="4"/><path d="M40 30l28 20-28 20z" fill="#fff"/></svg>
  <p class="abs about-text">Aliquip ex ea commodo consequat. Duis aute irure dolor in reprehenderit in voluptate velit esse cillum dolore eu fugiat nulla pariatur. Excepteur sint occaecat cupidatat non proident, sunt in culpa qui officia...</p>
  <a class="abs btn btn-about">View More Info</a>
</section>

<section>
  <div class="abs news"></div>
  <h2 class="abs heading section-title news-title">Latest News</h2>
  <article class="abs card card-1">
    <div class="card-img" role="img" aria-label="Photo of a hand touching a digital world map and charts display" style="background:linear-gradient(135deg,#3a4a5e,#6f8aa6 60%,#2e3847)"></div>
    <h4>Aliquip Commodo Aonsequat</h4>
    <p>Vloreero eos et accusamuos et accusamuss etodilo<br>rsocimuupiditate non provident, similique...</p>
    <div class="meta"><span>&#9635; 20 JUN 2017</span><i>|</i><span>&#9633; Comments (05)</span></div>
  </article>
  <article class="abs card card-2">
    <div class="card-img" role="img" aria-label="Photo of hands holding a tablet showing report charts" style="background:linear-gradient(135deg,#6b6256,#d9d9d6 50%,#8a7f70)"></div>
    <h4>Aliquip Commodo Aonsequat</h4>
    <p>Vloreero eos et accusamuos et accusamuss etodilo<br>rsocimuupiditate non provident, similique...</p>
    <div class="meta"><span>&#9635; 20 JUN 2017</span><i>|</i><span>&#9633; Comments (05)</span></div>
  </article>
  <article class="abs card card-3">
    <div class="card-img" role="img" aria-label="Photo of people reviewing printed charts with a pen" style="background:linear-gradient(135deg,#e9ecef,#c9d3dc 55%,#9fb2c2)"></div>
    <h4>Aliquip Commodo Aonsequat</h4>
    <p>Vloreero eos et accusamuos et accusamuss etodilo<br>rsocimuupiditate non provident, similique...</p>
    <div class="meta"><span>&#9635; 20 JUN 2017</span><i>|</i><span>&#9633; Comments (05)</span></div>
  </article>
</section>

<section>
  <div class="abs quote"></div>
  <div class="abs quote-mark">&#8220;</div>
  <p class="abs quote-text">&nbsp;&nbsp;&nbsp;&nbsp;&nbsp;&nbsp;&nbsp;Lorem ipsum dolor sit amet, consectetur adipiscing elit, sed do eiusmod tempor incididunt ut labore et dolore magna aliqua. Ut enim ad minim veniam, quis nostrud exercitation ullamco laboris nisi ut aliquip ex ea commodo consequat. Duis aute irure dolor in reprehenderit in voluptate velit esse cillum dolore eu fugiat nulla pariatur. Excepteur sint occaecat cupidatat...</p>
  <svg class="abs arrow" style="left:116px" width="16" height="44" viewBox="0 0 16 44"><path d="M14 2L2 22l12 20" fill="none" stroke="#fff" stroke-opacity=".8" stroke-width="1.5"/></svg>
  <svg class="abs arrow" style="left:1066px" width="16" height="44" viewBox="0 0 16 44"><path d="M2 2l12 20L2 42" fill="none" stroke="#fff" stroke-opacity=".8" stroke-width="1.5"/></svg>
</section>

<footer>
  <div class="abs brand footer-brand"><span class="brand-mark"></span>Northvale Ltd</div>
  <div class="abs foot-col links">
    <h5>Quick Links</h5>
    <ul><li>Home</li><li>About us</li><li>Data Governance</li><li>Report Modelling</li><li>Business Intelligence</li><li>Data protection</li><li>Inquiries</li><li>Contact us</li></ul>
  </div>
  <div class="abs foot-col newsletter">
    <h5>Newsletter</h5>
    <p>Register your Email Address to get<br>information about us</p>
    <div class="email-field">Email Address</div>
    <a class="btn btn-sub">Subscribe</a>
  </div>
  <div class="abs foot-col contact">
    <h5>Contact Info</h5>
    <div class="row"><svg width="12" height="16" viewBox="0 0 12 16"><path d="M6 0a6 6 0 0 0-6 6c0 4.5 6 10 6 10s6-5.5 6-10a6 6 0 0 0-6-6zm0 8.5A2.5 2.5 0 1 1 6 3.5a2.5 2.5 0 0 1 0 5z" fill="#0f6db8"/></svg><span>Box 40100 # Northvale<br>&nbsp;&nbsp;Street Name;City-5335</span></div>
    <div class="row" style="margin-top:18px"><svg width="13" height="13" viewBox="0 0 24 24"><path d="M6.6 10.8a15 15 0 0 0 6.6 6.6l2.2-2.2a1 1 0 0 1 1-.25 11.4 11.4 0 0 0 3.6.57 1 1 0 0 1 1 1V20a1 1 0 0 1-1 1A17 17 0 0 1 3 4a1 1 0 0 1 1-1h3.5a1 1 0 0 1 1 1c0 1.25.2 2.45.57 3.57a1 1 0 0 1-.25 1z" fill="#0f6db8"/></svg><span>(+345) 555-0142</span></div>
    <div class="row" style="margin-top:18px"><svg width="14" height="11" viewBox="0 0 14 11"><rect width="14" height="11" rx="1" fill="#0f6db8"/><path d="M1 1.5l6 4.5 6-4.5" fill="none" stroke="#fff" stroke-width="1.2"/></svg><span>info@northvale.com</span></div>
  </div>
  <div class="abs divider"></div>
  <div class="abs copyright">Copyright © 2017, Northvale Ltd. All rights reserved.</div>
  <div class="abs social"><span></span><span></span><span></span><span></span></div>
</footer>

</body>
</html>
```